Design a homepage graphic to show a system journey

We have a software package for parents to update student information and manage school excursions we have attached a concept we like but are open to other ideas so long as they fit the following criteria.
1 It needs to be landscape across the page
2. They are showing a series of processes, each step has its own colour, see below
2.1 The first process is a parent updating their own and students information and approving excursions
2.2 The school then creates and manages the excursion this includes a compliance component
2.3 The school conducts the activity it should show some activity type pictures
2.4 Students return safely to school
3 There can be text boxes within the image to clarify functionality
4. The picture should make anyone watching it understand there is a series of
linked processes the system provides i.e. a journey
There should be the ability to click on each component to link to a specific part of the pager lower down, e.g if the person wanted to look at the school part by clicking on the school it would take them to more information, that information already exists so is not required.
Please review the attached concept diagram and use this a potential guide.
Schools
1 page

```html
<!DOCTYPE html>
<html lang="en">
<head>
<meta charset="utf-8">
<title>School Excursion Journey</title>
<link href="https://fonts.googleapis.com/css2?family=Roboto:wght@400;500;700&display=swap" rel="stylesheet">
<style>
:root{
  --yellow:#fdb913;
  --yellow-soft:#fde3a0;
  --teal:#14b89c;
  --teal-soft:#d3f1ec;
  --blue:#05a3b9;
  --blue-soft:#cdeef3;
  --orange:#fd5b03;
  --orange-soft:#ffd3bd;
  --navy:#0f1e31;
  --ink:#1f2a38;
  --grey:#8b9097;
  --white:#ffffff;
}
*{margin:0;padding:0;box-sizing:border-box}
html,body{width:1200px;height:5227px;overflow:hidden;background:var(--white)}
body{position:relative;font-family:"Roboto",Arial,sans-serif;color:var(--ink)}
a{color:inherit;text-decoration:none}
.abs{position:absolute}
.blob{position:absolute;display:block}

/* header */
.site-header .logo{left:77px;top:52px;font-size:28px;font-weight:700;letter-spacing:-0.5px}
.site-nav{left:548px;top:64px;display:flex;gap:47px;font-size:15px}
.contact-btn{left:950px;top:55px;width:126px;height:36px;border-radius:18px;background:var(--white);
  font-size:15px;display:flex;align-items:center;justify-content:center;box-shadow:0 2px 6px rgba(0,0,0,.08)}

.hero-title{left:132px;top:168px;width:520px;font-size:50px;font-weight:700;line-height:52px;color:#3a3f47}
.hero-text{left:132px;top:352px;width:487px;font-size:12px;line-height:16px;color:var(--grey)}

/* journey */
.journey{left:0;top:600px;width:1200px;height:760px}
.step-note{width:175px;font-size:9px;line-height:11px;color:var(--grey)}
.step-note h4{font-size:12px;font-weight:700;color:var(--ink);margin-bottom:8px}
.label{font-size:13px;font-weight:700}

.illus{position:absolute;border-radius:46% 54% 48% 52%/55% 45% 55% 45%}

/* content sections */
.section-title{font-size:50px;font-weight:700;color:#3a3f47;white-space:nowrap}
.section-copy{width:487px;font-size:12px;line-height:16px;color:var(--grey)}
.section-copy p{margin-bottom:14px}
.more-btn{width:127px;height:37px;border-radius:19px;color:var(--white);font-size:15px;
  display:flex;align-items:center;justify-content:center}
.more-teal{background:var(--teal)}
.more-blue{background:var(--blue)}
.more-orange{background:var(--orange)}
.more-yellow{background:var(--yellow)}

/* footer */
.site-footer{left:0;top:4858px;width:1200px;height:369px;background:var(--navy);color:var(--white)}
.footer-logo{left:0;width:1200px;top:4943px;text-align:center;font-size:28px;font-weight:500;color:var(--white)}
.footer-nav{left:0;width:1200px;top:5010px;display:flex;justify-content:center;gap:47px;font-size:15px;color:var(--white)}
.footer-input{left:451px;top:5055px;width:345px;height:30px;border-radius:15px;background:var(--white);border:0}
.send-btn{left:564px;top:5106px;width:120px;height:30px;border-radius:15px;background:var(--yellow);
  color:var(--navy);font-size:15px;display:flex;align-items:center;justify-content:center}
.footer-text{left:0;width:1200px;top:5154px;text-align:center;font-size:11px;line-height:14px;color:#46576e}
</style>
</head>
<body>

<!-- decorative blobs -->
<svg class="blob" style="left:720px;top:0" width="480" height="660" viewBox="0 0 480 660" aria-hidden="true">
  <path d="M170 0 C120 60 200 140 120 200 C40 260 -20 330 40 420 C100 520 230 480 300 560 C360 630 440 640 480 650 L480 0Z" fill="var(--yellow-soft)"/>
  <path d="M200 0 C150 70 230 150 150 210 C70 270 30 340 80 420 C140 500 250 470 320 540 C380 600 440 620 480 620 L480 0Z" fill="var(--yellow)"/>
</svg>

<svg class="blob" style="left:0;top:1218px" width="340" height="430" viewBox="0 0 340 430" aria-hidden="true">
  <path d="M0 0 C60 10 110 90 170 150 C230 200 340 200 320 290 C300 370 150 370 60 400 C30 410 10 420 0 430Z" fill="var(--teal-soft)"/>
  <path d="M0 10 C60 20 100 100 160 150 C220 200 330 210 310 290 C290 360 150 360 60 390 C30 400 10 405 0 410Z" fill="var(--teal)"/>
</svg>

<svg class="blob" style="left:880px;top:1975px" width="320" height="465" viewBox="0 0 320 465" aria-hidden="true">
  <path d="M320 0 C250 30 240 100 200 150 C150 210 10 200 0 300 C-10 400 130 470 230 450 C270 445 300 440 320 440Z" fill="var(--blue-soft)"/>
  <path d="M320 30 C260 60 250 120 210 170 C170 220 30 220 20 310 C10 400 140 450 240 435 C280 430 300 425 320 420Z" fill="var(--blue)"/>
</svg>

<svg class="blob" style="left:0;top:2890px" width="280" height="415" viewBox="0 0 280 415" aria-hidden="true">
  <path d="M0 0 C70 10 90 90 130 150 C170 200 280 200 270 290 C260 370 150 360 70 380 C30 390 10 405 0 415Z" fill="var(--orange-soft)"/>
  <path d="M0 20 C60 30 80 100 120 150 C160 200 260 210 250 290 C240 360 140 350 70 370 C30 380 10 390 0 400Z" fill="var(--orange)"/>
</svg>

<svg class="blob" style="left:870px;top:3790px" width="330" height="410" viewBox="0 0 330 410" aria-hidden="true">
  <path d="M330 0 C260 20 220 90 170 140 C110 200 0 170 10 270 C20 360 150 340 230 370 C270 385 300 400 330 410Z" fill="var(--yellow-soft)"/>
  <path d="M330 20 C270 40 230 100 185 150 C130 210 40 190 50 270 C60 350 170 330 240 355 C280 370 305 380 330 385Z" fill="var(--yellow)"/>
</svg>

<svg class="blob" style="left:0;top:4660px" width="320" height="200" viewBox="0 0 320 200" aria-hidden="true">
  <path d="M0 0 C50 10 70 60 120 95 C170 130 260 110 300 160 C310 175 312 190 312 200 L0 200Z" fill="var(--navy)"/>
</svg>

<!-- header -->
<header class="site-header">
  <div class="abs logo">LOGO</div>
  <nav class="abs site-nav">
    <a href="#step-parent">item 1</a><a href="#step-school">item 2</a><a href="#step-activity">item 3</a><a href="#step-return">item 4</a>
  </nav>
  <a class="abs contact-btn" href="#contact">Contact</a>
</header>

<h1 class="abs hero-title">Lorem ipsum dolor sit amet, consectetuer adipiscing elit, sed</h1>
<p class="abs hero-text">Lorem ipsum dolor sit amet, consectetuer adipiscing elit, sed diam nonummy nibh euismod tincidunt ut laoreet dolore magna aliquam erat volutpat. Ut wisi enim ad minim veniam, quis nostrud exerci tation ullamcorper suscipit lobortis nisl ut aliquip ex ea</p>

<!-- journey graphic -->
<div class="illus" role="img" aria-label="Illustration of a parent helping a child update details on a laptop" style="left:122px;top:630px;width:203px;height:162px;background:linear-gradient(135deg,#dff4f0,#c8ebe5)"></div>
<div class="illus" role="img" aria-label="Illustration of children playing a sack race outdoors" style="left:600px;top:620px;width:235px;height:142px;background:linear-gradient(135deg,#fbeee6,#f5e3da)"></div>
<div class="illus" role="img" aria-label="Illustration of a school staff member working at an office desk" style="left:365px;top:1178px;width:235px;height:162px;background:linear-gradient(135deg,#e6f4f7,#d5ecf1)"></div>
<div class="illus" role="img" aria-label="Illustration of a yellow school bus returning with music notes" style="left:883px;top:1178px;width:244px;height:162px;background:linear-gradient(135deg,#fff4d6,#fde9b0)"></div>

<svg class="abs" style="left:0;top:600px" width="1200" height="700" viewBox="0 600 1200 700" aria-label="Four linked steps of the excursion journey">
  <!-- track -->
  <g fill="none" stroke-width="30" stroke-linecap="butt">
    <path d="M83 1010 L83 928 A126 126 0 0 1 335 928 C335 975 345 990 345 1039" stroke="var(--teal)"/>
    <path d="M345 1039 A126 126 0 0 0 597 1039 C597 990 605 975 605 928" stroke="var(--blue)"/>
    <path d="M605 928 A126 126 0 0 1 857 928 C857 975 865 990 865 1039" stroke="var(--orange)"/>
    <path d="M865 1039 A126 126 0 0 0 1117 1039 L1117 960" stroke="var(--yellow)"/>
  </g>
  <path d="M83 1010 L83 928 A126 126 0 0 1 335 928 C335 975 345 990 345 1039 A126 126 0 0 0 597 1039 C597 990 605 975 605 928 A126 126 0 0 1 857 928 C857 975 865 990 865 1039 A126 126 0 0 0 1117 1039 L1117 960"
        fill="none" stroke="var(--white)" stroke-width="3" stroke-dasharray="14 12"/>

  <!-- step 1 -->
  <a href="#step-parent">
    <circle cx="209" cy="928" r="87" fill="var(--teal)"/>
    <g fill="none" stroke="var(--white)" stroke-width="3" stroke-linejoin="round">
      <path d="M185 895 h36 l14 14 v56 h-50z"/><path d="M221 895 v14 h14"/>
      <path d="M195 920 h28 M195 932 h28 M195 944 h16"/>
      <circle cx="226" cy="952" r="9"/><path d="M222 952 l3 3 l5 -6"/>
    </g>
  </a>
  <!-- step 2 -->
  <a href="#step-school">
    <circle cx="471" cy="1039" r="87" fill="var(--blue)"/>
    <g fill="none" stroke="var(--white)" stroke-width="3" stroke-linejoin="round">
      <path d="M450 1010 h38 v52 M456 1004 h38 v52"/>
      <rect x="444" y="1016" width="38" height="56"/>
      <path d="M452 1030 h22 M452 1040 h22 M452 1050 h22"/>
      <circle cx="456" cy="1062" r="5"/>
    </g>
  </a>
  <!-- step 3 -->
  <a href="#step-activity">
    <circle cx="731" cy="928" r="87" fill="var(--orange)"/>
    <g fill="none" stroke="var(--white)" stroke-width="3" stroke-linejoin="round">
      <rect x="702" y="900" width="58" height="62"/>
      <path d="M714 894 v12 M726 894 v12 M738 894 v12 M750 894 v12"/>
      <path d="M731 914 l5 11 l12 1 l-9 8 l3 12 l-11 -6 l-11 6 l3 -12 l-9 -8 l12 -1z"/>
    </g>
  </a>
  <!-- step 4 -->
  <a href="#step-return">
    <circle cx="991" cy="1039" r="87" fill="var(--yellow)"/>
    <g fill="none" stroke="var(--white)" stroke-width="3" stroke-linejoin="round" stroke-linecap="round">
      <path d="M991 1080 C960 1055 948 1040 948 1022 C948 1005 962 996 975 998 C983 999 988 1004 991 1010 C994 1004 999 999 1007 998 C1020 996 1034 1005 1034 1022 C1034 1040 1022 1055 991 1080z"/>
      <path d="M1008 1033 h-34 M984 1023 l-10 10 l10 10"/>
    </g>
  </a>

  <!-- pointers -->
  <path d="M459 916 h24 l-12 13z" fill="var(--blue)"/>
  <path d="M979 916 h24 l-12 13z" fill="var(--yellow)"/>
  <path d="M197 1057 h24 l-12 -13z" fill="var(--teal)"/>
  <path d="M715 1057 h24 l-12 -13z" fill="var(--orange)"/>

  <!-- accents -->
  <path d="M388 664 L440 652 L428 686Z" fill="none" stroke="var(--teal)" stroke-width="5" stroke-linejoin="round"/>
  <rect x="668" y="1240" width="38" height="38" fill="none" stroke="#f0295a" stroke-width="5" transform="rotate(-15 687 1259)"/>
  <circle cx="96" cy="1196" r="17" fill="none" stroke="#1f4e8a" stroke-width="5"/>
  <path d="M1117 820 h60 M1135 832 h42" stroke="var(--yellow)" stroke-width="5" stroke-linecap="round"/>
</svg>

<div class="abs label" style="left:81px;top:1001px">Start</div>
<div class="abs label" style="left:1078px;top:958px">Finish</div>

<div class="abs step-note" style="left:390px;top:774px">
  <h4>Lorem ipsum dolor sit</h4>
  Lorem ipsum dolor sit amet, consectetuer adipiscing elit, sed diam nonummy nibh euismod tincidunt ut laoreet dolore magna aliquam erat volutpat. Ut wisi enim ad minim veniam, quis nostrud exerci tation ullamcorper suscipit lobortis nisl ut
</div>
<div class="abs step-note" style="left:910px;top:774px">
  <h4>Lorem ipsum dolor sit</h4>
  Lorem ipsum dolor sit amet, consectetuer adipiscing elit, sed diam nonummy nibh euismod tincidunt ut laoreet dolore magna aliquam erat volutpat. Ut wisi enim ad minim veniam, quis nostrud exerci tation ullamcorper suscipit lobortis nisl ut
</div>
<div class="abs step-note" style="left:142px;top:1076px">
  <h4>Lorem ipsum dolor sit</h4>
  Lorem ipsum dolor sit amet, consectetuer adipiscing elit, sed diam nonummy nibh euismod tincidunt ut laoreet dolore magna aliquam erat volutpat. Ut wisi enim ad minim veniam, quis nostrud exerci tation ullamcorper suscipit lobortis nisl ut
</div>
<div class="abs step-note" style="left:662px;top:1076px">
  <h4>Lorem ipsum dolor sit</h4>
  Lorem ipsum dolor sit amet, consectetuer adipiscing elit, sed diam nonummy nibh euismod tincidunt ut laoreet dolore magna aliquam erat volutpat. Ut wisi enim ad minim veniam, quis nostrud exerci tation ullamcorper suscipit lobortis nisl ut
</div>

<!-- section 1: parent -->
<section id="step-parent">
  <h2 class="abs section-title" style="left:132px;top:1670px">Lorem ipsum dolor sit</h2>
  <div class="abs section-copy" style="left:132px;top:1745px">
    <p>Lorem ipsum dolor sit amet, consectetuer adipiscing elit, sed diam nonummy nibh euismod tincidunt ut laoreet dolore magna aliquam erat volutpat. Ut wisi enim ad minim veniam, quis nostrud exerci tation ullamcorper suscipit lobortis nisl ut aliquip ex ea</p>
    <p>Lorem ipsum dolor sit amet, consectetuer adipiscing elit, sed diam nonummy nibh euismod tincidunt ut laoreet dolore magna aliquam erat volutpat. Ut wisi enim ad minim veniam, quis nostrud exerci tation ullamcorper suscipit lobortis nisl ut aliquip ex ea</p>
    <p>Lorem ipsum dolor sit amet, consectetuer adipiscing elit, sed diam nonummy nibh euismod tincidunt ut laoreet dolore magna aliquam erat volutpat. Ut wisi enim ad</p>
  </div>
  <a class="abs more-btn more-teal" style="left:132px;top:1965px" href="#step-parent">More...</a>
  <div class="illus" role="img" aria-label="Illustration of a parent helping a child update details on a laptop" style="left:650px;top:1695px;width:446px;height:315px;background:linear-gradient(135deg,#e3f5f2,#c9ece6)"></div>
</section>

<!-- section 2: school -->
<section id="step-school">
  <div class="illus" role="img" aria-label="Illustration of a school staff member working at an office desk" style="left:61px;top:2517px;width:426px;height:284px;background:linear-gradient(135deg,#e9f5f8,#d2ebf0)"></div>
  <h2 class="abs section-title" style="left:579px;top:2498px">Lorem ipsum dolor sit</h2>
  <div class="abs section-copy" style="left:579px;top:2573px">
    <p>Lorem ipsum dolor sit amet, consectetuer adipiscing elit, sed diam nonummy nibh euismod tincidunt ut laoreet dolore magna aliquam erat volutpat. Ut wisi enim ad minim veniam, quis nostrud exerci tation ullamcorper suscipit lobortis nisl ut aliquip ex ea</p>
    <p>Lorem ipsum dolor sit amet, consectetuer adipiscing elit, sed diam nonummy nibh euismod tincidunt ut laoreet dolore magna aliquam erat volutpat. Ut wisi enim ad minim veniam, quis nostrud exerci tation ullamcorper suscipit lobortis nisl ut aliquip ex ea</p>
    <p>Lorem ipsum dolor sit amet, consectetuer adipiscing elit, sed diam nonummy nibh euismod tincidunt ut laoreet dolore magna aliquam erat volutpat. Ut wisi enim ad</p>
  </div>
  <a class="abs more-btn more-blue" style="left:579px;top:2793px" href="#step-school">More...</a>
</section>

<!-- section 3: activity -->
<section id="step-activity">
  <h2 class="abs section-title" style="left:132px;top:3405px">Lorem ipsum dolor sit</h2>
  <div class="abs section-copy" style="left:132px;top:3480px">
    <p>Lorem ipsum dolor sit amet, consectetuer adipiscing elit, sed diam nonummy nibh euismod tincidunt ut laoreet dolore magna aliquam erat volutpat. Ut wisi enim ad minim veniam, quis nostrud exerci tation ullamcorper suscipit lobortis nisl ut aliquip ex ea</p>
    <p>Lorem ipsum dolor sit amet, consectetuer adipiscing elit, sed diam nonummy nibh euismod tincidunt ut laoreet dolore magna aliquam erat volutpat. Ut wisi enim ad minim veniam, quis nostrud exerci tation ullamcorper suscipit lobortis nisl ut aliquip ex ea</p>
    <p>Lorem ipsum dolor sit amet, consectetuer adipiscing elit, sed diam nonummy nibh euismod tincidunt ut laoreet dolore magna aliquam erat volutpat. Ut wisi enim ad</p>
  </div>
  <a class="abs more-btn more-orange" style="left:132px;top:3700px" href="#step-activity">More...</a>
  <div class="illus" role="img" aria-label="Illustration of children playing a sack race outdoors" style="left:680px;top:3390px;width:467px;height:315px;background:linear-gradient(135deg,#fbefe8,#f4e2d8)"></div>
</section>

<!-- section 4: return -->
<section id="step-return">
  <div class="illus" role="img" aria-label="Illustration of a yellow school bus returning with music notes and sunshine" style="left:57px;top:4233px;width:430px;height:315px;background:linear-gradient(135deg,#fff5da,#fde7ad)"></div>
  <h2 class="abs section-title" style="left:579px;top:4233px">Lorem ipsum dolor sit</h2>
  <div class="abs section-copy" style="left:579px;top:4308px">
    <p>Lorem ipsum dolor sit amet, consectetuer adipiscing elit, sed diam nonummy nibh euismod tincidunt ut laoreet dolore magna aliquam erat volutpat. Ut wisi enim ad minim veniam, quis nostrud exerci tation ullamcorper suscipit lobortis nisl ut aliquip ex ea</p>
    <p>Lorem ipsum dolor sit amet, consectetuer adipiscing elit, sed diam nonummy nibh euismod tincidunt ut laoreet dolore magna aliquam erat volutpat. Ut wisi enim ad minim veniam, quis nostrud exerci tation ullamcorper suscipit lobortis nisl ut aliquip ex ea</p>
    <p>Lorem ipsum dolor sit amet, consectetuer adipiscing elit, sed diam nonummy nibh euismod tincidunt ut laoreet dolore magna aliquam erat volutpat. Ut wisi enim ad</p>
  </div>
  <a class="abs more-btn more-yellow" style="left:577px;top:4533px" href="#step-return">More...</a>
</section>

<!-- footer -->
<footer id="contact">
  <div class="abs site-footer"></div>
  <div class="abs footer-logo">LOGO</div>
  <nav class="abs footer-nav">
    <a href="#step-parent">item 1</a><a href="#step-school">item 2</a><a href="#step-activity">item 3</a><a href="#step-return">item 4</a>
  </nav>
  <input class="abs footer-input" type="email" aria-label="Email address">
  <a class="abs send-btn" href="#contact">Send...</a>
  <p class="abs footer-text">Lorem ipsum dolor sit amet, consectetuer adipiscing elit, sed diam nonummy nibh<br>euismod tincidunt ut laoreet dolore magna aliquam erat volutpat. Ut wisi enim ad</p>
</footer>

</body>
</html>
```